Gutscheine
Zielgruppe
Immobilienmakler, Verkauf und Vermietung, Immobilienbewertung
Aufgabenstellung
Es soll eine Gutscheinkarte werden für die Verteilung auf einen Stadtfest am Stand vor unserem Büro.
Es soll ein Bezug zu Immobilien haben, aber auch eine Emotion vermitteln. Daher Bild mit Familie oder Rentner. Zielgruppe sollen sein zum einen junge Leute, die vor haben eine Immobilie zu kaufen. Und auf der anderen Seite Leute, die mit dem Gedanken spielen eine Immobilie aus Altersgründen, Trennung, Scheidung oder nach Erbe zu verkaufen. Dominant soll mit dem Gutschein zur kostenlosen Bewertung einer Immobilie gelockt werden.
Auf der Rückseite soll es so sein, dass Kunden ankreuzen können, ob Sie eine Immobilie evtl. Verkaufen möchten und eine kostenlose Bewertung wünschen.
Evtl. macht es Sinn zwei Karten anzulegen. Einmal Zielgruppe Käufer/Suchende, einmal Verkäufer.
Beim Format bin ich flexibel und für alles . Es kann länglich sein, aber auch quadratisch.
Vom Design einen Bezug zu den bisherigen Flyern und Broschüren im Anhang.
Bilder die auf der Homepage sind, sind als Stockbilder vorhanden.
Es werden noch einige andere Sachen für das Stadtfest benötigt. Wie Bierdeckel, Imagebroschüre zum Aufklappen, Banner, Roll-Up, Luftballons.

```html
<!DOCTYPE html>
<html lang="de">
<head>
<meta charset="utf-8">
<title>Gutscheinkarten – Marwen Immobilien</title>
<link href="https://fonts.googleapis.com/css2?family=Playfair+Display:wght@400&family=Ubuntu:wght@400&display=swap" rel="stylesheet">
<style>
  :root{
    --stage:#5a5a5a;
    --paper:#ffffff;
    --navy:#1f3566;
    --gold:#c2a753;
    --ink:#222a3a;
    --text-navy:#1e3366;
  }
  *{box-sizing:border-box;margin:0;padding:0}
  html,body{width:1200px;height:600px;overflow:hidden;background:var(--stage)}
  .sheet{position:relative;width:1200px;height:600px}
  .card{position:absolute;width:558px;height:263px;background:var(--paper);overflow:hidden;font-family:"Ubuntu",sans-serif}
  .card--front-sell{left:30px;top:18px}
  .card--front-buy{left:617px;top:18px}
  .card--back-sell{left:30px;top:314px}
  .card--back-buy{left:617px;top:314px}

  .photo{position:absolute;left:0;top:0;width:365px;height:263px}
  .photo--seniors{background:linear-gradient(90deg,rgba(255,255,255,0) 60%,#fff 100%),linear-gradient(180deg,#e9e6d6 0%,#c9b6a6 55%,#b89a86 100%)}
  .photo--family{background:linear-gradient(90deg,rgba(255,255,255,0) 80%,#fff 100%),linear-gradient(180deg,#6f9ad8 0%,#b9cde8 40%,#c9d6d8 62%,#8db56a 100%)}

  .frame{position:absolute;left:26px;top:26px;height:105px;border-left:2px solid;border-top:2px solid}
  .frame--light{width:336px;border-color:rgba(255,255,255,.9)}
  .frame--navy{width:469px;border-color:var(--navy)}

  .title-panel{position:absolute;left:0;top:180px;width:261px;height:83px;background:rgba(255,255,255,.82);border-top:3px solid var(--gold)}
  .title-panel::after{content:"";position:absolute;right:-8px;top:-3px;width:8px;height:86px;background:var(--navy)}
  .title{position:absolute;left:26px;bottom:16px;font-family:"Playfair Display",serif;font-size:50px;line-height:1;color:var(--navy);font-weight:400}

  .brand-square{position:absolute;left:491px;top:26px;width:39px;height:39px;background:var(--gold);outline:1px solid #e3d3a4;outline-offset:2px}
  .accent-line{position:absolute;left:530px;top:89px;width:2px;height:50px}
  .accent-line--gold{background:var(--gold)}
  .accent-line--navy{background:var(--navy)}

  .offer{position:absolute;right:27px;top:152px;text-align:right;font-size:15.5px;line-height:21px;letter-spacing:.6px;color:var(--text-navy)}

  .back-bg{position:absolute;inset:0;background:linear-gradient(90deg,#fff 0%,rgba(255,255,255,.6) 45%,rgba(255,255,255,.2) 100%),linear-gradient(180deg,#f4f1ea 0%,#ece6da 60%,#e6dccb 100%)}
  .back-bottom{position:absolute;left:0;bottom:0;width:296px;height:26px;background:#fff}
  .back-bar{position:absolute;left:296px;bottom:0;width:8px;height:26px;background:var(--navy)}

  .prompt{position:absolute;left:26px;top:50px;font-family:"Playfair Display",serif;font-size:24px;color:var(--navy);font-weight:400}
  .option{position:absolute;left:26px;font-size:11.5px;letter-spacing:.5px;color:var(--ink)}
  .option .box{position:absolute;left:0;width:11px;height:11px;border:1.5px solid var(--ink)}
  .option .label{position:absolute;left:25px;white-space:nowrap}
  .phone-field{position:absolute;left:26px;top:200px;font-size:11.5px;letter-spacing:.5px;color:var(--ink);white-space:nowrap}

  .brand{position:absolute;left:440px;top:27px;width:94px;text-align:center}
  .brand .brand-mark{display:block;width:57px;height:57px;margin:0 auto;background:var(--gold);outline:1px solid #d9c68e;outline-offset:2px}
  .brand .brand-name{display:block;margin-top:11px;font-size:21px;letter-spacing:3px;color:var(--navy);line-height:1}
  .brand .brand-sub{display:block;margin-top:3px;font-size:6px;letter-spacing:1.5px;color:var(--navy)}

  .contact{position:absolute;left:440px;top:186px;font-size:8px;line-height:11.4px;letter-spacing:.4px;color:var(--ink)}
  .contact .row{position:relative;padding-left:11px}
  .contact svg{position:absolute;left:0;top:1px}
</style>
</head>
<body>
<div class="sheet">

  <section class="card card--front-sell">
    <div class="photo photo--seniors" role="img" aria-label="Älteres Paar von hinten vor einem Haus, sonnig und verblasst"></div>
    <div class="frame frame--light"></div>
    <div class="brand-square"></div>
    <div class="accent-line accent-line--gold"></div>
    <div class="title-panel"><h1 class="title">Gutschein</h1></div>
    <p class="offer">Kostenlose<br>Wertermittlung<br>&amp; Verkaufsberatung<br>für Eigentümer</p>
  </section>

  <section class="card card--front-buy">
    <div class="photo photo--family" role="img" aria-label="Familie mit Kindern und Fußball vor einem modernen Haus mit Garten"></div>
    <div class="frame frame--navy"></div>
    <div class="brand-square"></div>
    <div class="accent-line accent-line--navy"></div>
    <div class="title-panel"><h1 class="title">Gutschein</h1></div>
    <p class="offer">Kostenlose<br>Immobilienbewertung<br>&amp; Beratung für<br>Kaufinteressenten</p>
  </section>

  <section class="card card--back-sell">
    <div class="back-bg" role="img" aria-label="Heller, verblasster Wohnraum mit Treppe und Sofa"></div>
    <div class="back-bottom"></div>
    <div class="back-bar"></div>
    <h2 class="prompt">Bitte ankreuzen</h2>
    <div class="option" style="top:107px"><span class="box"></span><span class="label" style="top:-2px">Ich möchte den realen Wert meiner Immobilie erfahren</span></div>
    <div class="option" style="top:145px"><span class="box"></span><span class="label" style="top:10px">Ich erwäge einen Verkauf</span></div>
    <p class="phone-field">Telefon: ________________________________________</p>
    <div class="brand"><span class="brand-mark"></span><span class="brand-name">MARWEN</span><span class="brand-sub">IMMOBILIEN</span></div>
    <div class="contact">
      <div class="row"><svg width="8" height="8" viewBox="0 0 24 24" fill="none" stroke="#222a3a" stroke-width="2"><path d="M5 3h4l2 5-3 2a12 12 0 0 0 6 6l2-3 5 2v4a2 2 0 0 1-2 2A17 17 0 0 1 3 5a2 2 0 0 1 2-2z"/></svg>01234 56 78 900</div>
      <div class="row" style="margin-top:4px"><svg width="8" height="9" viewBox="0 0 24 26" fill="none" stroke="#222a3a" stroke-width="2"><path d="M12 24s8-8 8-14a8 8 0 0 0-16 0c0 6 8 14 8 14z"/><circle cx="12" cy="10" r="3"/></svg>Marwen Immobilien<br>Lindenallee 12<br>50999 Talheim<br>Deutschland</div>
    </div>
  </section>

  <section class="card card--back-buy">
    <div class="back-bg" role="img" aria-label="Heller, verblasster Wohnraum mit Treppe und Sofa"></div>
    <div class="back-bottom"></div>
    <div class="back-bar"></div>
    <h2 class="prompt">Bitte ankreuzen</h2>
    <div class="option" style="top:105px"><span class="box"></span><span class="label" style="top:-2px">Ich suche eine Immobilie zum Kauf</span></div>
    <div class="option" style="top:152px"><span class="box"></span><span class="label" style="top:-2px">Ich möchte eine kostenlose Immobilienbewertung</span></div>
    <p class="phone-field" style="top:198px;left:29px">Telefon: ________________________________________</p>
    <div class="brand"><span class="brand-mark"></span><span class="brand-name">MARWEN</span><span class="brand-sub">IMMOBILIEN</span></div>
    <div class="contact">
      <div class="row"><svg width="8" height="8" viewBox="0 0 24 24" fill="none" stroke="#222a3a" stroke-width="2"><path d="M5 3h4l2 5-3 2a12 12 0 0 0 6 6l2-3 5 2v4a2 2 0 0 1-2 2A17 17 0 0 1 3 5a2 2 0 0 1 2-2z"/></svg>01234 56 78 900</div>
      <div class="row" style="margin-top:4px"><svg width="8" height="9" viewBox="0 0 24 26" fill="none" stroke="#222a3a" stroke-width="2"><path d="M12 24s8-8 8-14a8 8 0 0 0-16 0c0 6 8 14 8 14z"/><circle cx="12" cy="10" r="3"/></svg>Marwen Immobilien<br>Lindenallee 12<br>50999 Talheim<br>Deutschland</div>
    </div>
  </section>

</div>
</body>
</html>
```